Biz Card for Harrowfield Property Partners - HWPP

Harrowfield Property Partners is a commercial real estate acquisitions firm. We buy commercial property and need to raise capital from investors for each deal we buy. The vibe needs to be: give us your money, we will multiply it.
Our website: www.hrwpp-example.com
Competitors are: https://velmarholdings-example.com/, https://tribanquepartners-example.com/, http://www.ostrellecapital-example.com/
Target Market(s)
High Net Worth Individuals, Bankers, Insurance Companies, Commercial Real Estate Brokers.
Industry/Entity Type
Investment Banking
Contact Information for Business Card
Name, Title, Addess, Cell#, Office#, email, website
Requirements
Must have
- use one of our logos. See website for look and feel: www.hrwpp-example.com
Nice to have
- see website: www.hrwpp-example.com

```html
<!DOCTYPE html>
<html lang="en">
<head>
<meta charset="utf-8">
<title>Harrowfield Property Partners – Business Card</title>
<link rel="stylesheet" href="https://fonts.googleapis.com/css2?family=Montserrat:wght@400;500;700&family=Roboto:wght@400;500&display=swap">
<style>
  :root {
    --backdrop: #d9d9d7;
    --paper: #ffffff;
    --ink: #1a1a1a;
    --ink-soft: #2b2b2b;
    --muted: #444444;
    --watermark: #f0f0f0;
    --card-dark: #141414;
    --card-dark-mid: #3a3a3a;
    --mark-light: #ffffff;
  }
  * { box-sizing: border-box; margin: 0; padding: 0; }
  html, body {
    width: 1200px; height: 801px; overflow: hidden;
    background: var(--backdrop);
  }
  .stage {
    position: relative; width: 1200px; height: 801px;
    display: flex; align-items: center; justify-content: center; gap: 40px;
  }
  .card {
    position: relative; width: 540px; height: 309px; overflow: hidden;
    box-shadow: 0 6px 18px rgba(0,0,0,0.18);
  }
  /* Front */
  .card-front { background: var(--paper); color: var(--ink); }
  .watermark-disc {
    position: absolute; left: 280px; top: -60px; width: 220px; height: 220px;
    border-radius: 50%; background: var(--watermark);
  }
  .brand {
    position: absolute; left: 32px; top: 58px;
    font-family: "Montserrat", sans-serif; font-weight: 400; color: var(--ink);
  }
  .brand-name { font-size: 25px; letter-spacing: 6px; line-height: 1; }
  .brand-sub { font-size: 8.5px; letter-spacing: 5px; margin-top: 6px; }
  .person {
    position: absolute; left: 74px; top: 128px;
    font-family: "Montserrat", sans-serif;
  }
  .person-name { font-weight: 700; font-size: 13px; letter-spacing: 0.3px; }
  .person-title { font-weight: 500; font-size: 11.5px; color: var(--ink-soft); margin-top: 1px; }
  .contact-list {
    position: absolute; left: 74px; top: 176px; list-style: none;
    font-family: "Roboto", sans-serif; font-size: 14px; color: var(--ink-soft);
  }
  .contact-item { display: flex; align-items: center; gap: 8px; height: 21px; }
  .contact-icon { width: 13px; height: 13px; flex: none; }
  .address {
    position: absolute; right: 34px; top: 188px; text-align: right;
    font-family: "Roboto", sans-serif; font-size: 14px; line-height: 19px; color: var(--muted);
  }
  /* Back */
  .card-back { background: var(--card-dark); }
  .back-pattern {
    position: absolute; inset: 0;
    background: linear-gradient(115deg, var(--card-dark-mid) 0%, #262626 40%, var(--card-dark) 75%);
  }
  .back-mark {
    position: absolute; left: 418px; top: 140px; width: 62px; height: 62px;
    border-radius: 50%; background: var(--mark-light);
  }
</style>
</head>
<body>
<main class="stage">
  <section class="card card-front" aria-label="Business card front">
    <div class="watermark-disc" aria-hidden="true"></div>
    <div class="brand">
      <div class="brand-name">HARROWFIELD</div>
      <div class="brand-sub">PROPERTY PARTNERS</div>
    </div>
    <div class="person">
      <div class="person-name">MARCUS ELLINGTON</div>
      <div class="person-title">Managing Director</div>
    </div>
    <ul class="contact-list">
      <li class="contact-item">
        <svg class="contact-icon" viewBox="0 0 13 13" aria-hidden="true"><rect x="3" y="0.5" width="7" height="12" rx="1.2" fill="none" stroke="currentColor" stroke-width="1.2"/><circle cx="6.5" cy="10.5" r="0.7" fill="currentColor"/></svg>
        555.214.0387
      </li>
      <li class="contact-item">
        <svg class="contact-icon" viewBox="0 0 13 13" aria-hidden="true"><path d="M1 4.5 Q6.5 1 12 4.5 L11 6 L9 5.2 L9 4 Q6.5 3 4 4 L4 5.2 L2 6 Z" fill="currentColor"/><rect x="2.5" y="7" width="8" height="5.5" rx="1" fill="currentColor"/></svg>
        555.602.4419
      </li>
      <li class="contact-item">
        <svg class="contact-icon" viewBox="0 0 13 13" aria-hidden="true"><rect x="0.5" y="2.5" width="12" height="8" fill="currentColor"/><path d="M0.5 2.5 L6.5 7.5 L12.5 2.5" fill="none" stroke="#fff" stroke-width="1"/></svg>
        marcus@hrwpp-example.com
      </li>
      <li class="contact-item">
        <svg class="contact-icon" viewBox="0 0 13 13" aria-hidden="true"><circle cx="6.5" cy="6.5" r="6" fill="currentColor"/><ellipse cx="6.5" cy="6.5" rx="2.6" ry="6" fill="none" stroke="#fff" stroke-width="0.8"/><path d="M0.5 6.5 H12.5" stroke="#fff" stroke-width="0.8"/></svg>
        www.hrwpp-example.com
      </li>
    </ul>
    <address class="address" style="font-style:normal">
      Linwood Crest Avenue, Suite<br>210 Harbor Point, USA
    </address>
  </section>

  <section class="card card-back" aria-label="Business card back">
    <div class="back-pattern" role="img" aria-label="Repeating pattern of glossy embossed brand-mark discs on black stock"></div>
    <div class="back-mark" aria-hidden="true"></div>
  </section>
</main>
</body>
</html>
```